Home change of address

Martin & Priya Colwell
WE HAVE MOVED
The address of our new home is
Birch Hollow
47 Thornbury Lane Road
Ashcombe on Wend
Warwickshire
B72 8QT
Tel: 07912 384071
Email: martin@pelmora.uk.com

```html
<!DOCTYPE html>
<html lang="en">
<head>
<meta charset="utf-8">
<title>Martin &amp; Priya Colwell – We Have Moved</title>
<link rel="stylesheet" href="https://fonts.googleapis.com/css2?family=Italiana&family=Outfit:wght@300;400&display=swap">
<style>
  :root {
    --ink: #312a2b;
    --paper: #ffffff;
    --leaf-deep: #6f8a4e;
    --leaf-mid: #9bb173;
    --olive-fruit: #a8cc4a;
  }
  * { margin: 0; padding: 0; box-sizing: border-box; }
  html, body { width: 1200px; height: 1200px; overflow: hidden; background: var(--paper); }
  .card {
    position: relative;
    width: 1200px;
    height: 1200px;
    background: var(--paper);
    color: var(--ink);
    font-family: "Outfit", sans-serif;
    overflow: hidden;
  }
  .foliage {
    position: absolute;
    width: 440px;
    height: 320px;
  }
  .foliage--top-left {
    top: 0; left: 0;
    background: radial-gradient(ellipse at 20% 20%, var(--leaf-mid) 0%, rgba(155,177,115,0.55) 35%, rgba(255,255,255,0) 72%);
  }
  .foliage--top-right {
    top: 0; right: 0;
    background: radial-gradient(ellipse at 80% 20%, var(--leaf-mid) 0%, rgba(155,177,115,0.55) 35%, rgba(255,255,255,0) 72%);
  }
  .foliage--bottom-left {
    bottom: 0; left: 0;
    height: 280px;
    background: radial-gradient(ellipse at 20% 80%, var(--leaf-mid) 0%, rgba(155,177,115,0.55) 35%, rgba(255,255,255,0) 72%);
  }
  .foliage--bottom-right {
    bottom: 0; right: 0;
    width: 380px;
    height: 280px;
    background: radial-gradient(ellipse at 80% 80%, var(--leaf-mid) 0%, rgba(155,177,115,0.55) 35%, rgba(255,255,255,0) 72%);
  }
  .couple-name {
    position: absolute;
    top: 262px;
    left: 0;
    width: 1200px;
    text-align: center;
    font-family: "Italiana", serif;
    font-weight: 400;
    font-size: 84px;
    line-height: 1;
    letter-spacing: 0;
    color: var(--ink);
  }
  .announcement {
    position: absolute;
    top: 385px;
    left: 385px;
    font-size: 51px;
    font-weight: 400;
    line-height: 1;
    letter-spacing: 0.5px;
  }
  .intro {
    position: absolute;
    top: 455px;
    left: 214px;
    font-size: 55px;
    font-weight: 400;
    line-height: 1;
  }
  .address {
    position: absolute;
    top: 558px;
    left: 214px;
    font-style: normal;
    font-size: 45px;
    font-weight: 300;
    line-height: 55px;
  }
</style>
</head>
<body>
  <main class="card">
    <div class="foliage foliage--top-left" role="img" aria-label="Olive branch with green leaves and olives"></div>
    <div class="foliage foliage--top-right" role="img" aria-label="Olive branch with green leaves and olives"></div>
    <div class="foliage foliage--bottom-left" role="img" aria-label="Olive branch with green leaves and olives"></div>
    <div class="foliage foliage--bottom-right" role="img" aria-label="Olive branch with green leaves and olives"></div>

    <h1 class="couple-name">Martin &amp; Priya Colwell</h1>
    <p class="announcement">WE HAVE MOVED</p>
    <p class="intro">The address of our new home is</p>

    <address class="address">
      Birch Hollow<br>
      47 Thornbury Lane Road<br>
      Ashcombe on Wend<br>
      Warwickshire<br>
      B72 8QT<br>
      Tel: 07912 384071<br>
      Email: martin@pelmora.uk.com
    </address>
  </main>
</body>
</html>
```